Website design for management consulting firm

We need a web design for a new consulting company based in Boston, MA called "Quillmoor Ridge Consulting." This webpage will be simple home page, with a "contact us" page, that describes the services of the consulting firm. The company provides strategic planning, business assessment, process re-designs, and other management consulting functions. I would like the website to look high-tech. A logo was already created via Artsy Hive.

Target Market(s)

Other business owners across a wide spectrum of industries - from IT to retail.

Industry/Entity Type

It Company

Number of Pages Required

3 page

Colors
0455a3
ffffff

Requirements
Must have
• Front page that provides generic text / overview of the firm. A "services" tab that describes consulting services. A "contact us" tab that provides either a form to contact us or just the contact email address of the company. info@quillmoorridgeconsulting.example

```html
<!DOCTYPE html>
<html lang="en">
<head>
<meta charset="utf-8">
<title>Quillmoor Ridge Consulting</title>
<link href="https://fonts.googleapis.com/css2?family=Raleway:wght@300;400;500&family=Open+Sans:wght@400;600&display=swap" rel="stylesheet">
<style>
  :root {
    --ink: #050607;
    --navy: #04467f;
    --teal: #17a89a;
    --teal-bright: #1fb3a5;
    --ocean: #05628a;
    --ocean-line: #0a5878;
    --white: #ffffff;
    --band: #1d2124;
    --card-active: #5d5f61;
    --button-grey: #e4e6e8;
    --button-text: #2a5a86;
  }
  * { box-sizing: border-box; margin: 0; padding: 0; }
  html, body { width: 1081px; height: 1200px; overflow: hidden; background: var(--ink); }
  .page { position: relative; width: 1081px; height: 1200px; font-family: 'Raleway', sans-serif; color: var(--white); }

  /* Header */
  .site-header { position: absolute; top: 0; left: 0; width: 1081px; height: 119px; background: var(--ink); }
  .brand { position: absolute; left: 43px; top: 14px; height: 83px; display: flex; align-items: center; gap: 16px; }
  .brand-mark { width: 83px; height: 83px; background: var(--ocean); }
  .brand-name { font-family: 'Raleway', sans-serif; font-weight: 500; font-size: 30px; line-height: 1.05; color: var(--white); width: 300px; }
  .main-nav { position: absolute; top: 0; left: 523px; height: 119px; display: flex; }
  .main-nav a { display: flex; align-items: center; height: 119px; font-family: 'Open Sans', sans-serif; font-size: 12px; font-weight: 600; color: var(--white); text-decoration: none; letter-spacing: .2px; }
  .main-nav .nav-home { width: 78px; justify-content: center; background: var(--navy); margin-right: 40px; }
  .main-nav .nav-about { margin-right: 60px; }
  .main-nav .nav-services { margin-right: 61px; }

  /* Hero */
  .hero { position: absolute; top: 119px; left: 0; width: 1081px; height: 506px;
    background: radial-gradient(ellipse at 62% 60%, #8c7b74 0%, #5c5f68 30%, #3a4656 60%, #252c36 100%); }
  .hero-title { position: absolute; top: 150px; left: 0; width: 1081px; text-align: center; font-weight: 300; }
  .hero-title .line-accent { display: block; font-size: 66px; color: var(--teal); letter-spacing: 1px; line-height: 78px; margin-left: -20px; }
  .hero-title .line-main { display: block; font-size: 70px; color: var(--white); letter-spacing: 1px; line-height: 86px; }
  .slider-dots { position: absolute; left: 1015px; top: 171px; width: 28px; height: 140px; border-radius: 14px; background: rgba(8,60,90,.75);
    display: flex; flex-direction: column; align-items: center; justify-content: space-evenly; padding: 8px 0; }
  .slider-dots span { width: 9px; height: 9px; border-radius: 50%; background: var(--white); }
  .slider-dots span.is-active { background: var(--teal); border: 1px solid var(--white); }

  /* Services */
  .services { position: absolute; top: 625px; left: 0; width: 1081px; height: 269px; background: linear-gradient(180deg, #25292c, #16191b); }
  .service { position: absolute; top: 0; width: 250px; height: 269px; text-align: center; }
  .service.is-active { background: var(--card-active); }
  .service-icon { position: absolute; top: 34px; left: 50%; transform: translateX(-50%); }
  .service h3 { position: absolute; top: 116px; left: 0; width: 100%; font-size: 16px; font-weight: 500; color: var(--teal); }
  .service p { position: absolute; top: 143px; left: 0; width: 100%; font-size: 12.5px; line-height: 15px; color: #e8e8e8; }
  .service .more { position: absolute; top: 200px; left: 50%; transform: translateX(-50%); width: 64px; height: 28px; line-height: 28px;
    font-size: 11px; font-family: 'Open Sans', sans-serif; background: var(--button-grey); color: var(--button-text); border-radius: 2px; }
  .service.is-active .more { background: var(--teal); color: var(--white); }

  /* Footer info */
  .info { position: absolute; top: 894px; left: 0; width: 1081px; height: 240px; background: var(--ocean); font-family: 'Open Sans', sans-serif; }
  .info .divider { position: absolute; top: 14px; width: 1px; height: 210px; background: var(--ocean-line); }
  .info h4 { position: absolute; font-family: 'Raleway', sans-serif; font-size: 15.5px; font-weight: 500; letter-spacing: .2px; }
  .info p { position: absolute; font-size: 10.6px; line-height: 15.3px; }
  .about-text { left: 45px; top: 68px; width: 330px; text-align: justify; }
  .read-more { position: absolute; left: 46px; top: 186px; width: 94px; height: 34px; background: var(--teal); font-size: 11px; line-height: 34px; text-align: center; }
  .email-field { position: absolute; left: 471px; top: 127px; width: 266px; height: 33px; background: var(--white); color: #a8a8a8; font-size: 10.5px; line-height: 33px; padding-left: 11px; }
  .subscribe { position: absolute; left: 471px; top: 170px; width: 266px; height: 33px; background: var(--teal); font-size: 14px; line-height: 33px; text-align: center; letter-spacing: .5px; }
  .contact-list { position: absolute; left: 843px; top: 66px; list-style: none; font-size: 11px; line-height: 15.3px; letter-spacing: .3px; }
  .contact-list li { position: relative; padding-left: 26px; margin-bottom: 5px; }
  .contact-list svg { position: absolute; left: 0; top: 2px; }

  /* Bottom bar */
  .site-footer { position: absolute; top: 1134px; left: 0; width: 1081px; height: 66px; background: #000; }
  .copyright { position: absolute; top: 27px; left: 0; width: 1081px; text-align: center; font-size: 10px; color: var(--white); }
  .social { position: absolute; top: 20px; left: 946px; display: flex; gap: 7px; }
  .social span { width: 26px; height: 25px; border: 1px solid var(--navy); }
  .social span.is-filled { background: var(--navy); }
</style>
</head>
<body>
<div class="page">

  <header class="site-header">
    <div class="brand">
      <div class="brand-mark"></div>
      <div class="brand-name">Quillmoor Ridge Consulting</div>
    </div>
    <nav class="main-nav">
      <a class="nav-home" href="#">HOME</a>
      <a class="nav-about" href="#">ABOUT US</a>
      <a class="nav-services" href="#">SERVICES</a>
      <a class="nav-contact" href="#">CONTACT US</a>
    </nav>
  </header>

  <section class="hero" role="img" aria-label="Blurred photo of hands working on a tablet at a desk">
    <h1 class="hero-title">
      <span class="line-accent">PROGRESSIVE</span>
      <span class="line-main">BUSINESS THINKING</span>
    </h1>
    <div class="slider-dots">
      <span></span><span></span><span class="is-active"></span><span></span><span></span>
    </div>
  </section>

  <section class="services">
    <article class="service is-active" style="left:54px; width:241px;">
      <svg class="service-icon" width="56" height="52" viewBox="0 0 56 52" fill="var(--teal-bright)">
        <circle cx="12" cy="10" r="6"/><circle cx="44" cy="10" r="6"/>
        <path d="M2 32c0-8 4-13 10-13s10 5 10 13z"/><path d="M34 32c0-8 4-13 10-13s10 5 10 13z"/>
        <circle cx="28" cy="16" r="9"/><path d="M12 52c0-13 7-22 16-22s16 9 16 22z"/>
      </svg>
      <h3>Strategic Planning</h3>
      <p>Lorem ipsum dolor sit amet,<br>consectetur adipiscing elit, sed<br>do eiusmod tempor labour</p>
      <div class="more">MORE</div>
    </article>
    <article class="service" style="left:298px;">
      <svg class="service-icon" width="50" height="46" viewBox="0 0 50 46" fill="none" stroke="var(--teal-bright)" stroke-width="5" stroke-linejoin="round">
        <path d="M25 4 L45 14 L25 24 L5 14 Z"/><path d="M5 26 L25 36 L45 26"/>
      </svg>
      <h3 style="top:113px;">Business Assessment</h3>
      <p style="top:140px;">Lorem ipsum dolor sit amet,<br>consectetur adipiscing elit, sed<br>do eiusmod tempor labour</p>
      <div class="more">MORE</div>
    </article>
    <article class="service" style="left:551px;">
      <svg class="service-icon" width="52" height="52" viewBox="0 0 52 52" fill="none" stroke="var(--teal-bright)">
        <circle cx="26" cy="26" r="21" stroke-width="8"/><circle cx="26" cy="26" r="11" stroke="#1d2124" stroke-width="3"/>
        <g stroke="#1d2124" stroke-width="4"><path d="M12 12l8 8M40 12l-8 8M12 40l8-8M40 40l-8-8"/></g>
      </svg>
      <h3>Process Re-designs</h3>
      <p style="top:145px;">Lorem ipsum dolor sit amet,<br>consectetur adipiscing elit, sed<br>do eiusmod tempor labour</p>
      <div class="more" style="top:201px; height:31px;">MORE</div>
    </article>
    <article class="service" style="left:804px;">
      <svg class="service-icon" width="44" height="52" viewBox="0 0 44 52" fill="none" stroke="var(--teal-bright)" stroke-width="3.5">
        <path d="M3 2h26l12 12v36H3z"/><path d="M29 2v12h12"/><path d="M11 24h22M11 31h22M11 38h22"/>
      </svg>
      <h3>Management Consulting</h3>
      <p style="top:151px;">Lorem ipsum dolor sit amet,<br>consectetur adipiscing elit, sed<br>do eiusmod tempor labour</p>
      <div class="more">MORE</div>
    </article>
  </section>

  <section class="info">
    <h4 style="left:47px; top:32px;">ABOUT US</h4>
    <p class="about-text">Lorem ipsum dolor sit amet, consectetur adipiscing elit, sed do eiusmod tempor incididunt ut labore et dolore magna aliqua. Ut enim ad minim veniam, quis nostrud exercitation ullamco laboris nisi ut aliquip ex ea commodo consequat. Duis aute irure dolor in reprehenderit in voluptate velit esse cillum dolore eu fugiat nulla pariatur.</p>
    <div class="read-more">READ MORE</div>

    <div class="divider" style="left:420px;"></div>

    <h4 style="left:469px; top:34px;">NEWSLETTER SIGNUP</h4>
    <p style="left:469px; top:68px; width:280px;">Subscribe our newsletter to know our daily updates and offer daily updates and offerpsun dolor sit amet elit, sed aliqua.</p>
    <div class="email-field">Enter your Email Id</div>
    <div class="subscribe">SUBSCRIBE</div>

    <div class="divider" style="left:797px;"></div>

    <h4 style="left:850px; top:32px;">LOCATION</h4>
    <ul class="contact-list">
      <li><svg width="10" height="13" viewBox="0 0 10 13" fill="#fff"><path d="M5 0a5 5 0 0 1 5 5c0 3-5 8-5 8S0 8 0 5a5 5 0 0 1 5-5z"/><circle cx="5" cy="5" r="2" fill="#05628a"/></svg>Address Line1,<br>Address Line-2<br>Lorem ipsum dolor<br>Country - 123456</li>
      <li><svg width="11" height="11" viewBox="0 0 11 11" fill="#fff"><path d="M2 0l2 3-1 1.5c.8 1.6 1.9 2.7 3.5 3.5L8 7l3 2-1 2C5 11 0 6 0 1z"/></svg>Office:&nbsp; 123.456.789</li>
      <li><svg width="11" height="11" viewBox="0 0 11 11" fill="#fff"><rect x="2" y="0" width="7" height="4"/><rect x="0" y="4" width="11" height="7" rx="1"/><rect x="3" y="6" width="5" height="1.5" fill="#05628a"/></svg>Fax:&nbsp; 123.456.789</li>
      <li><svg width="11" height="9" viewBox="0 0 11 9" fill="#fff"><rect width="11" height="9"/><path d="M0 0l5.5 5L11 0" stroke="#05628a" fill="none"/></svg>info@companyname.com</li>
    </ul>
  </section>

  <footer class="site-footer">
    <p class="copyright">Copyright 2015 Comapny name. All Rights Reserved.</p>
    <div class="social">
      <span aria-label="Professional network profile"></span>
      <span class="is-filled" aria-label="Microblog profile"></span>
      <span aria-label="Social network page"></span>
    </div>
  </footer>

</div>
</body>
</html>
```